Solvane Travel Planners needs an bold logo and business card design

Thanks you all for helping me with this project your assistance is appriciated
I am starting a home based travel agency and I need a bold and eye catching logo and business card designed.
I want to convey a sense of FREEDOM, expertise, customer service for travel customers
Solvane travel planners is a full service travel agency focused on customer service and adding value to a vacation and travel planning.
my idea is for a card that looks like an cruise ship boarding pass or passport with stamps with a back drop of beautiful beach scene, resort hotel and happiness.
The logo should be eye catching, unique but give a sense of freedom and it should be travel related
We want to give customers a sense of Freedom from travel planning, freedom from researching cruises and hotels and freedom to enjoy a wonderful cost effective vacation.

Target Market(s)

Customers considering travel for vacations, family reunions, business and weddings

Industry/Entity Type

Travel Industry

Contact Information for Business Card

Solvane Travel Planners
Marcus Helbrook Owner
MHelbrook@SolvaneTravelPlanners.com
SolvaneTravelPlanners.com
(555) 214-7830

Logo Text

“One’s destination is never a place, but a new way of seeing things.”

Font styles to use
Serif

Colors
85cae6
0492cd
ec1f27
e667a6
b768aa
33b8a4

Requirements
Must have
• The Logo you create should be on the busoness card
• should be clean, easy to read and attractive
• something you that would make you want to work with a travel agent
Nice to have
• should have cruise ship, hotel on the card or something that conveys travel
Should not have
• Should not have the american flag
• no yellow on the card

```html
<!DOCTYPE html>
<html lang="en">
<head>
<meta charset="utf-8">
<title>Solvane Travel Planners – Business Card</title>
<link rel="stylesheet" href="https://fonts.googleapis.com/css2?family=Playfair+Display:wght@400;700;900&family=Jost:wght@300;400;600&display=swap">
<style>
  :root {
    --backdrop: #d5d9da;
    --card-light: #acd4dc;
    --card-navy: #2f3165;
    --ink: #22244f;
    --ink-soft: #c9e2e8;
    --edge: #b8985f;
  }
  * { box-sizing: border-box; margin: 0; padding: 0; }
  html, body { width: 1200px; height: 1200px; overflow: hidden; }
  body {
    background: var(--backdrop);
    position: relative;
    font-family: "Jost", sans-serif;
    color: var(--ink);
  }
  .card {
    position: absolute;
    left: 220px;
    width: 760px;
    height: 434px;
    box-shadow: 0 14px 30px rgba(0,0,0,0.12);
  }
  /* Front */
  .card-front { top: 110px; background: var(--card-light); }
  .contact { position: absolute; left: 58px; top: 52px; width: 460px; }
  .contact-name, .contact-role {
    font-family: "Playfair Display", serif;
    font-weight: 900;
    font-size: 38px;
    line-height: 1.1;
    display: inline-block;
    border-bottom: 3px solid var(--ink);
    padding-bottom: 4px;
  }
  .contact-role { font-size: 32px; margin-top: 22px; }
  .rule { height: 3px; background: var(--ink); margin: 22px 0; }
  .rule-short { width: 300px; }
  .contact-web { font-size: 17px; line-height: 1.45; font-weight: 400; }
  .contact-phone { font-size: 40px; font-weight: 300; letter-spacing: 1px; }
  .front-mark {
    position: absolute; right: 58px; bottom: 60px;
    display: flex; align-items: center; gap: 14px;
    font-family: "Jost", sans-serif; font-weight: 600; font-size: 20px;
    text-transform: uppercase; letter-spacing: 1px; line-height: 1.15;
    text-align: left;
  }
  .front-mark .dot {
    width: 70px; height: 70px; border-radius: 50%;
    border: 4px solid var(--ink);
  }
  /* Back */
  .card-back {
    top: 660px; background: var(--card-navy); color: var(--ink-soft);
    border-bottom: 6px solid var(--edge);
  }
  .passport-title {
    position: absolute; left: 48px; top: 36px;
    font-family: "Playfair Display", serif; font-weight: 400;
    font-size: 84px; letter-spacing: 4px;
  }
  .ship-art {
    position: absolute; left: 60px; top: 170px;
    width: 300px; height: 200px;
    background: linear-gradient(160deg, #b6d9e0, #8fbac6);
    border-radius: 4px;
  }
  .back-mark {
    position: absolute; left: 420px; top: 200px;
    font-family: "Jost", sans-serif; font-weight: 600; font-size: 34px;
    text-transform: uppercase; letter-spacing: 2px; line-height: 1.1;
  }
  .chip { position: absolute; right: 52px; bottom: 44px; }
</style>
</head>
<body>
  <section class="card card-front">
    <div class="contact">
      <div class="contact-name">Marcus Helbrook</div><br>
      <div class="contact-role">Owner</div>
      <div class="rule"></div>
      <div class="contact-web">MHelbrook@SolvaneTravelPlanners.com<br>SolvaneTravelPlanners.com</div>
      <div class="rule"></div>
      <div class="contact-phone">(555) 214-7830</div>
      <div class="rule rule-short"></div>
    </div>
    <div class="front-mark">
      <span class="dot"></span>
      <span>Solvane<br>Travel Planners</span>
    </div>
  </section>

  <section class="card card-back">
    <div class="passport-title">PASSPORT</div>
    <div class="ship-art" role="img" aria-label="Illustration of a cruise ship"></div>
    <div class="back-mark">Solvane<br>Travel<br>Planners</div>
    <svg class="chip" width="70" height="46" viewBox="0 0 70 46" aria-hidden="true">
      <rect x="2" y="2" width="66" height="42" rx="3" fill="none" stroke="var(--ink-soft)" stroke-width="4"/>
      <line x1="2" y1="23" x2="68" y2="23" stroke="var(--ink-soft)" stroke-width="4"/>
      <circle cx="35" cy="23" r="9" fill="var(--card-navy)" stroke="var(--ink-soft)" stroke-width="4"/>
    </svg>
  </section>
</body>
</html>
```